Sports Psychology Business Card Design

Need a catchy and unique business card design for our sport psychology practice. We provide mental performance counseling and consulting to performers from all types of industries with a special emphases on athletes.The name of our practice is "Steady Core of Achievement" or "SCA" as is indicated in the logo examples submitted in this brief. Also provided were logos with specific sports referenced which represent sources of our clients from those sports.

Target Market(s)

Executives, Professionals (doctors, lawyers, etc.), Athletes, Entertainers and other performers

Contact Information for Business Card

Need to include our logo (logos provided in this brief).

Font styles to use
Other font styles liked:
• Font can be found in logo

Colors
0792cd
34a7d8
85cae6

Requirements
Must have
• Our logo and reference to our provision of mental performance counseling/consulting/coaching
Nice to have
• References to sports that our athletes play as provided in the brief.
Should not have
• This is not a general wellness consulting practice. Our focus is on consulting to improve mental performance.

```html
<!DOCTYPE html>
<html lang="en">
<head>
<meta charset="utf-8">
<title>Steady Core of Achievement – Business Card</title>
<link href="https://fonts.googleapis.com/css2?family=Nunito:wght@400;700;800&display=swap" rel="stylesheet">
<style>
  :root {
    --backdrop: #ebebeb;
    --paper: #f2f2f2;
    --ink: #23272b;
    --brand-blue: #1a6fb5;
    --reverse-text: #f4f4f4;
  }
  html, body {
    margin: 0;
    padding: 0;
    width: 1200px;
    height: 1200px;
    overflow: hidden;
    background: var(--backdrop);
    font-family: "Nunito", sans-serif;
  }
  .card {
    position: absolute;
    left: 227px;
    width: 745px;
    height: 425px;
    box-sizing: border-box;
  }
  .card--front { top: 135px; background: var(--paper); color: var(--ink); }
  .card--back  { top: 638px; background: var(--ink); color: var(--reverse-text); }

  .wordmark {
    position: absolute;
    display: flex;
    align-items: center;
    gap: 14px;
    font-weight: 800;
    line-height: 1;
    letter-spacing: 2px;
  }
  .wordmark__dot {
    width: 20px;
    height: 20px;
    border-radius: 50%;
    background: var(--brand-blue);
    flex: none;
  }
  .card--front .wordmark {
    top: 62px;
    left: 0;
    right: 0;
    justify-content: center;
    font-size: 106px;
    color: var(--ink);
  }
  .card--back .wordmark {
    top: 170px;
    left: 76px;
    font-size: 82px;
    color: var(--reverse-text);
  }

  .holder {
    position: absolute;
    left: 0;
    right: 0;
    text-align: center;
  }
  .holder__name {
    top: 248px;
    font-size: 23px;
    font-weight: 800;
    color: var(--brand-blue);
    letter-spacing: 0.3px;
  }
  .holder__role {
    top: 279px;
    font-size: 17px;
    font-weight: 400;
  }
  .divider {
    position: absolute;
    top: 319px;
    left: 349px;
    width: 47px;
    height: 5px;
    background: var(--brand-blue);
  }
  .contact {
    position: absolute;
    left: 0;
    right: 0;
    text-align: center;
    font-size: 22px;
    letter-spacing: 1px;
  }
  .contact--primary { top: 341px; }
  .contact--web { top: 372px; font-size: 19px; letter-spacing: 1.2px; }
  .contact__sep { color: var(--brand-blue); margin: 0 12px; }
  .contact__accent { color: var(--brand-blue); }

  .tagline {
    position: absolute;
    top: 172px;
    left: 339px;
    margin: 0;
    font-size: 26px;
    font-weight: 800;
    line-height: 38px;
    letter-spacing: 3.5px;
    text-transform: uppercase;
    color: var(--reverse-text);
  }
</style>
</head>
<body>
  <section class="card card--front">
    <div class="wordmark"><span>SCA</span><span class="wordmark__dot"></span></div>
    <div class="holder holder__name">DANA WHITFIELD</div>
    <div class="holder holder__role">Mental Performance Consultant</div>
    <div class="divider"></div>
    <div class="contact contact--primary">555-014-7391<span class="contact__sep">/</span>dana@thesca.co</div>
    <div class="contact contact--web">www.<span class="contact__accent">thesca</span>.co</div>
  </section>

  <section class="card card--back">
    <div class="wordmark"><span>SCA</span><span class="wordmark__dot"></span></div>
    <p class="tagline">The Steady Core<br>of Achievement</p>
  </section>
</body>
</html>
```